Web Design Project

need a website, logo and a matching business Card for design studio. i have a company that works with many companies and i want to offer design services that will be outsourced to craftflock.

this website is totally for the design services. i need it to be simple but very catcgy and trendy, yet MUST BE ELEGENT.

you being a designer will know best what do i require in this website and how it should look and feel..

i dont need many pages, most of the selling work to clients will be face to face, this is just for them to view the sample works.

the company is called "Corvelin, Vividra Studio", so pages i need are: 1- the Studio 2- Folios 3- Contact us( will include company informaiton, and online contact form that should have a drop-down list of all types of designs.

main focus is the folios pages, it needs to have samples of works, the classification of works should be on two basis, by type of design and by designer. client should be able to select a certain designer and send an inquiry. if the customer does that, then i should get all client details and the designer should get a notification that he has been requested though no contact details of client should be given to designer as i want to make sure that those jobs are given to designer through craft flock and this is an invitation for any designer who care to put his works on the website. next to that, if the customer requires a job online then we need to get information on how design should feel and look.

please quote your price to include the website and business card design, A3 head letter and envelope.

Please provide a mock up of your design or a briefing an initial design before asking to be announced as the winner.

my customers are general managers and decision makers.

Business

• ability to filiter works based on type or designer. and website must offer all types of designs included here

```html
<!DOCTYPE html>
<html lang="en">
<head>
<meta charset="utf-8">
<title>Corvelin Vividra Studio</title>
<link href="https://fonts.googleapis.com/css2?family=Questrial&family=Advent+Pro:wght@200;300&family=Open+Sans:ital,wght@0,400;0,600;1,400&display=swap" rel="stylesheet">
<style>
  :root {
    --page-top: #d3cfc9;
    --page-bg: #f4f4f4;
    --white: #ffffff;
    --line: #dddddd;
    --panel: #f2f2f2;
    --orange: #f29a00;
    --orange-dark: #c86a00;
    --ink: #4a4a4a;
    --ink-soft: #777777;
    --price: #8a6a4a;
    --sky: #7cb4d6;
    --footer: #e6e6e6;
    --social-a: #8aa8dc;
    --social-b: #8fd0ec;
  }
  * { box-sizing: border-box; margin: 0; padding: 0; }
  html, body { width: 1200px; height: 979px; overflow: hidden; }
  body {
    position: relative;
    background: var(--page-bg);
    font-family: "Open Sans", Arial, sans-serif;
    color: var(--ink);
  }
  .page-band { position: absolute; left: 0; top: 0; width: 1200px; height: 360px; }
  .site {
    position: absolute; left: 67px; top: 16px; width: 1066px; height: 938px;
    background: var(--white); border: 1px solid #e2e2e2;
  }
  .brand {
    position: absolute; left: 20px; top: 20px;
    font-family: "Questrial", sans-serif; font-size: 31px; color: var(--ink);
    letter-spacing: 0.5px;
  }
  .nav { position: absolute; left: 739px; top: 24px; display: flex; }
  .nav a {
    display: block; width: 105px; height: 34px; line-height: 34px;
    background: var(--orange); color: var(--white); text-align: center;
    text-decoration: none; font-size: 17px; border-left: 1px solid #ffc35e;
  }
  .nav a:first-child { border-left: none; }
  .hero {
    position: absolute; left: 11px; top: 81px; width: 1044px; height: 466px;
    overflow: hidden;
  }
  .hero-art {
    position: absolute; inset: 0;
    background:
      radial-gradient(circle at 50% 40%, rgba(255,190,80,0.95) 0, rgba(210,100,20,0.7) 90px, rgba(60,20,5,0.3) 230px, transparent 320px),
      linear-gradient(90deg, #4a2a08 0%, #1a0c05 25%, #070505 50%, #05101a 78%, #123848 92%, #2a0d40 100%);
  }
  .hero-tagline {
    position: absolute; top: 210px;
    font-family: "Advent Pro", sans-serif; font-weight: 200;
    font-size: 56px; color: #e8e8e8; letter-spacing: 1px;
  }
  .hero-tagline.left { left: 168px; }
  .hero-tagline.right { left: 614px; }
  .hero-cta {
    position: absolute; left: 812px; top: 411px; width: 209px; height: 38px;
    background: var(--sky); color: var(--white); text-decoration: none;
    font-family: "Advent Pro", sans-serif; font-weight: 300; font-size: 23px;
    display: flex; align-items: center; padding-left: 14px; gap: 14px;
  }
  .services {
    position: absolute; left: 11px; top: 559px; width: 1044px; height: 301px;
    border: 1px solid var(--line);
  }
  .services-inner {
    position: absolute; left: 10px; top: 10px; width: 1022px; height: 278px;
    background: var(--panel); border: 1px solid #e4e4e4;
  }
  .service { position: absolute; top: 20px; width: 216px; }
  .service-card {
    height: 193px; background: var(--white); border: 1px solid #dcdcdc;
    position: relative;
  }
  .service-title {
    text-align: center; font-size: 25px; color: var(--ink); padding-top: 10px;
  }
  .price-badge {
    position: absolute; left: 12px; top: 71px; width: 108px; height: 108px;
    border-radius: 50%;
    background: radial-gradient(circle, #fdf9f1 55%, #efe3cf 100%);
    box-shadow: 0 2px 5px rgba(0,0,0,0.15);
    text-align: center; color: var(--price);
  }
  .price-badge .from { display: block; margin-top: 20px; font-style: italic; font-size: 15px; color: #9a8a78; }
  .price-badge .amount { display: block; font-weight: 600; font-size: 33px; line-height: 36px; }
  .service-art { position: absolute; border-radius: 4px; }
  .learn-more {
    display: block; margin: 28px auto 0; width: 100px; height: 21px; line-height: 20px;
    border: 1px solid #cfcfcf; border-radius: 10px; text-align: center;
    background: linear-gradient(#fafafa, #e2e2e2); color: #444; font-size: 12px;
    text-decoration: none;
  }
  .slider-arrow {
    position: absolute; top: 108px; width: 40px; height: 44px;
    background: var(--white); border: 1px solid #dcdcdc; border-radius: 22px;
    display: flex; align-items: center; justify-content: center;
  }
  .slider-arrow.prev { left: -4px; }
  .slider-arrow.next { left: 996px; }
  .footer {
    position: absolute; left: 11px; top: 882px; width: 1044px; height: 42px;
    background: var(--footer);
  }
  .legal { position: absolute; left: 14px; top: 13px; font-size: 11.5px; color: #555; }
  .legal a { color: var(--orange-dark); text-decoration: none; }
  .join { position: absolute; left: 917px; top: 13px; font-style: italic; font-size: 12.5px; color: #555; }
  .social { position: absolute; top: 2px; width: 36px; height: 36px; }
  .social.one { left: 970px; background: var(--social-a); }
  .social.two { left: 1007px; background: var(--social-b); }
</style>
</head>
<body>
  <svg class="page-band" viewBox="0 0 1200 360" aria-hidden="true">
    <polygon points="0,0 1200,0 1200,290 1133,360 67,360 0,326" fill="#d3cfc9"/>
  </svg>

  <div class="site">
    <div class="brand">Corvelin Vividra Studio</div>
    <nav class="nav">
      <a href="#">The Studio</a>
      <a href="#">Folios</a>
      <a href="#">Contact Us</a>
    </nav>

    <section class="hero">
      <div class="hero-art" role="img" aria-label="Glowing light bulb on a dark background with soft light streaks"></div>
      <div class="hero-tagline left">Your Business</div>
      <div class="hero-tagline right">Our Creativity</div>
      <a class="hero-cta" href="#">View Our Folios
        <svg width="22" height="16" viewBox="0 0 22 16"><path d="M1 8H20M13 1l7 7-7 7" stroke="#fff" stroke-width="1.6" fill="none"/></svg>
      </a>
    </section>

    <section class="services">
      <div class="services-inner">
        <div class="slider-arrow prev"><svg width="10" height="18" viewBox="0 0 10 18"><path d="M9 1 1 9l8 8" stroke="#444" stroke-width="1.4" fill="none"/></svg></div>

        <div class="service" style="left:32px">
          <div class="service-card">
            <div class="service-title">Logo Design</div>
            <div class="price-badge"><span class="from">Starting at</span><span class="amount">$240</span></div>
            <div class="service-art" role="img" aria-label="Red ink splash illustration" style="left:120px;top:140px;width:70px;height:62px;background:#d42a25;border-radius:40%"></div>
          </div>
          <a class="learn-more" href="#">Learn More</a>
        </div>

        <div class="service" style="left:272px">
          <div class="service-card">
            <div class="service-title">Business Card</div>
            <div class="price-badge"><span class="from">Starting at</span><span class="amount">$130</span></div>
            <div class="service-art" role="img" aria-label="Business card samples" style="left:105px;top:132px;width:104px;height:74px;background:linear-gradient(135deg,#ffffff,#e4e4e4);border:1px solid #ccc"></div>
          </div>
          <a class="learn-more" href="#">Learn More</a>
        </div>

        <div class="service" style="left:512px">
          <div class="service-card">
            <div class="service-title">Stationery</div>
            <div class="price-badge"><span class="from">Starting at</span><span class="amount">$200</span></div>
            <div class="service-art" role="img" aria-label="Stationery set samples" style="left:125px;top:132px;width:82px;height:72px;background:linear-gradient(135deg,#ffffff,#ececec);border:1px solid #ccc"></div>
          </div>
          <a class="learn-more" href="#">Learn More</a>
        </div>

        <div class="service" style="left:752px">
          <div class="service-card">
            <div class="service-title">Web Design</div>
            <div class="price-badge"><span class="from">Starting at</span><span class="amount">$320</span></div>
            <div class="service-art" role="img" aria-label="Website layout sample" style="left:130px;top:132px;width:78px;height:72px;background:linear-gradient(#f3f3f3,#e0e0e0);border:1px solid #ccc"></div>
          </div>
          <a class="learn-more" href="#">Learn More</a>
        </div>

        <div class="slider-arrow next"><svg width="10" height="18" viewBox="0 0 10 18"><path d="M1 1l8 8-8 8" stroke="#444" stroke-width="1.4" fill="none"/></svg></div>
      </div>
    </section>

    <footer class="footer">
      <p class="legal">Copyright © 2012 Corvelin Vividra Studio. Use of this website constitutes acceptance of our <a href="#">User Agreement</a>, <a href="#">Privacy Policy</a> and <a href="#">money back refund policy</a>.</p>
      <span class="join">Join Us</span>
      <span class="social one" role="img" aria-label="Social network link"></span>
      <span class="social two" role="img" aria-label="Social network link"></span>
    </footer>
  </div>
</body>
</html>
```